2 Page Business Flyer for Finance Business

Need a two page flyer created for a finance business. Lots of text and needs to fit on two pages.

Corporate business/banking look and feel. Not too many large images. Lots of white space, clean design. Attached is color palette and the text contents of the flyer.

```html
<!DOCTYPE html>
<html lang="en">
<head>
<meta charset="utf-8">
<title>Vanilla Options – Two Page Flyer</title>
<link href="https://fonts.googleapis.com/css2?family=Open+Sans:wght@300;400;600&family=Source+Sans+3:wght@400&display=swap" rel="stylesheet">
<style>
:root{
  --backdrop:#d9d9d9;
  --cream:#eddcbc;
  --tan:#d8bf88;
  --gold:#e3c37e;
  --coral:#d9473e;
  --navy:#1f2142;
  --slate:#3f4269;
  --lavender:#5b5d8e;
  --ink:#2b2a35;
  --light:#e7dcc6;
  --photo-sky-a:#6d8fb8;
  --photo-sky-b:#1f2d4a;
  --photo-desk-a:#7a5a3c;
  --photo-desk-b:#2a1c12;
  --photo-garden-a:#6f8a5a;
  --photo-garden-b:#2c4a49;
}
*{margin:0;padding:0;box-sizing:border-box}
html,body{width:1200px;height:941px;overflow:hidden}
body{background:var(--backdrop);font-family:'Source Sans 3',sans-serif;position:relative}
.page{position:absolute;overflow:hidden}
.page svg.bg{position:absolute;left:0;top:0}
.page-one{left:28px;top:73px;width:562px;height:796px;background:var(--cream)}
.page-two{left:613px;top:73px;width:564px;height:796px;background:var(--navy)}
.abs{position:absolute}
ul{list-style:none}

.title-tag{left:0;top:91px;width:330px;height:51px;background:var(--coral);
  clip-path:polygon(0 0,100% 0,94% 100%,0 100%);color:#fff;font-family:'Open Sans',sans-serif;font-size:17px;font-weight:400;line-height:19px;padding-top:7px}
.title-tag .l1{padding-left:25px}
.title-tag .l2{text-align:right;padding-right:28px}

.body-copy{font-size:9px;line-height:11.2px;color:var(--ink)}
.body-copy p{margin-bottom:11.2px}
.col-left{left:48px;top:283px;width:244px}
.col-right{left:312px;top:283px;width:204px}
.example{left:48px;top:527px;width:244px}

.steps{left:0;top:411px;width:296px;height:97px;background:var(--tan);
  clip-path:polygon(0 0,100% 0,95% 100%,0 100%);padding:8px 0 0 48px}
.steps li{font-size:9px;line-height:11.2px;color:var(--ink);margin-bottom:8px;padding-left:8px;position:relative;width:215px}
.steps li::before{content:"•";position:absolute;left:0}

.band-title{font-family:'Open Sans',sans-serif;font-size:15.5px;font-weight:400;color:var(--gold);margin-bottom:7px;line-height:20px}
.band-list li{font-size:9px;line-height:11.2px;color:var(--light);padding-left:8px;position:relative}
.band-list li::before{content:"-";position:absolute;left:0}
.characteristics{left:48px;top:641px;width:225px}
.advantages{left:312px;top:641px;width:200px}

.risks-label{left:0;top:17px;width:120px;height:53px;background:var(--navy);color:var(--coral);font-family:'Open Sans',sans-serif;font-size:27px;line-height:53px;padding-left:27px;font-weight:400}
.risks-note{left:114px;top:17px;width:450px;height:53px;background:var(--lavender);clip-path:polygon(10px 0,100% 0,100% 100%,0 100%);
  color:var(--gold);font-family:'Open Sans',sans-serif;font-size:13.5px;line-height:15.5px;font-weight:600;padding:11px 0 0 24px}
.why-title{left:48px;top:236px;color:var(--gold);font-family:'Open Sans',sans-serif;font-size:20.5px;line-height:27px;font-weight:600}
.why-copy{left:48px;top:297px;width:214px;color:var(--light);font-family:'Open Sans',sans-serif;font-size:13.8px;line-height:18.2px;font-weight:300;letter-spacing:-0.1px}
.price-intro{left:305px;top:276px;width:210px;color:var(--light);font-size:9.3px;line-height:13.2px}
.factors{left:305px;top:408px;width:215px}
.factors li{font-size:9.3px;line-height:13.2px;color:var(--ink);margin-bottom:13.6px;position:relative}
.factors li.style{margin-top:26px}
</style>
</head>
<body>

<section class="page page-one">
  <svg class="bg" width="562" height="796" viewBox="0 0 562 796">
    <defs>
      <linearGradient id="skyline" x1="0" y1="0" x2="1" y2="1">
        <stop offset="0" stop-color="var(--photo-sky-a)"/>
        <stop offset="1" stop-color="var(--photo-sky-b)"/>
      </linearGradient>
    </defs>
    <polygon role="img" aria-label="Photo of glass office towers against a cloudy sky" points="0,0 562,0 562,83 300,243 0,243" fill="url(#skyline)"/>
    <polygon points="0,243 300,243 562,83 562,120 302,252 0,252" fill="var(--coral)"/>
    <polygon points="0,629 562,629 562,775 0,775" fill="var(--navy)"/>
    <polygon points="0,629 294,629 274,775 0,775" fill="var(--slate)"/>
  </svg>

  <h1 class="abs title-tag"><div class="l1">HOW DOES A VANILLA OPTION</div><div class="l2">CONTRACT WORK?</div></h1>

  <div class="abs body-copy col-left">
    <p>The buyer of a vanilla option receives protection against an adverse movement in the exchange rate while allowing full participation in a beneficial move. At no time is the buyer of a Vanilla Option obligated to exercise the Option and transact the currencies, therefore providing flexibility in cases where the requirement to purchase foreign currency is not certain.</p>
    <p>A buyer of vanilla options is required to pay a premium (like an insurance premium) for the right, but not the obligation, to exchange currency at a predetermined rate on a predetermined date.</p>
  </div>

  <ul class="abs steps">
    <li>Set a protection rate which will be your worst-case scenario at expiry</li>
    <li>Determine the amount of currency you wish to protect</li>
    <li>Choose an expiry date for the contract</li>
    <li>Calculate the premium you are required to pay</li>
  </ul>

  <div class="abs body-copy example">
    <p>Let’s look at an example: You are in importer.<br>Your construction company has bid on a project that if successful, will require you to import materials from the United States to use in construction. You have used todays pricing of materials in calculating your bid and want to protect against an adverse move in the US dollar exchange rate from eroding your margin if your bid is chosen for the project.</p>
  </div>

  <div class="abs body-copy col-right">
    <p>You choose to buy a Vanilla Call which will protect you from a rise in the USD/CAD exchange rate above your protection rate. You choose to buy protection on $500,000 USD, with a protection rate (strike rate) of 1.3300 expiring 3 months from now. You are required to pay a premium which in this case is calculated to be 1.8%, or 11,970 CAD.</p>
    <p>Your bid is successful: If the exchange rate is below your protection rate at expiration, you have no obligation relating to the vanilla call and you are free to buy USD at the cheaper spot rate. If the exchange rate is above your protection rate, your have the right to purchase your USD at the protection rate, and thereby claiming your insurance policy.</p>
    <p>Your bid is not successful: You have no obligation relating to the vanilla option however, if at expiry the exchange rate is above the protection rate, you may exercise your right to buy USD at the lower rate and simultaneous sell USD back at the prevailing spot rate, thereby recouping some or all of the premium paid to buy the option.<br>Alternatively, if you find out your bid was not successful with time still left until expiration, you may sell your option back into the market in the case that it still has residual value, which will depend on various market factors.</p>
  </div>

  <div class="abs characteristics">
    <h3 class="band-title">CHARACTERISTICS</h3>
    <ul class="band-list">
      <li>You are looking for a straight-forward hedging solution</li>
      <li>You want to receive full benefit from an appreciation of the currency you are exposed to</li>
      <li>You are comfortable receiving protection at the strike rate of the option</li>
      <li>You are willing to pay the non-refundable premium</li>
    </ul>
  </div>

  <div class="abs advantages">
    <h3 class="band-title">ADVANTAGES</h3>
    <ul class="band-list">
      <li>You hedge your foreign currency exposure at a predefined hedge rate</li>
      <li>You can choose the hedge rate that suits your budget requirements</li>
      <li>Provides the ability to fully participate in a favourable exchange rate move</li>
      <li>You can choose from most major currency pairs to meet your needs</li>
    </ul>
  </div>
</section>

<section class="page page-two">
  <svg class="bg" width="564" height="796" viewBox="0 0 564 796">
    <defs>
      <linearGradient id="desk" x1="0" y1="0" x2="1" y2="1">
        <stop offset="0" stop-color="var(--photo-desk-a)"/>
        <stop offset="1" stop-color="var(--photo-desk-b)"/>
      </linearGradient>
      <linearGradient id="garden" x1="0" y1="0" x2="1" y2="1">
        <stop offset="0" stop-color="var(--photo-garden-a)"/>
        <stop offset="1" stop-color="var(--photo-garden-b)"/>
      </linearGradient>
    </defs>
    <polygon role="img" aria-label="Photo of hands signing a document on a wooden desk" points="0,0 564,0 564,243 265,243 0,82" fill="url(#desk)"/>
    <polygon points="0,82 265,243 564,243 564,250 262,250 0,118" fill="var(--coral)"/>
    <polygon points="283,391 564,391 564,796 247,796" fill="var(--tan)"/>
    <polygon role="img" aria-label="Photo of a smiling woman holding a phone outdoors" points="0,573 255,679 247,796 0,796" fill="url(#garden)"/>
  </svg>

  <div class="abs risks-label">RISKS</div>
  <div class="abs risks-note">Premium paid is non-refundable and remains your<br>only obligation when buying vanilla options</div>

  <h2 class="abs why-title">WHY USE<br>VANILLA OPTIONS?</h2>
  <p class="abs why-copy">Vanilla options are often compared to an insurance product. The buyer pays a non-refundable premium for the right, but not the obligation to trade currency in the future at the protection rate of the option. This product allows you to participate in a beneficial move to an unlimited extent, which will be the most advantageous outcome, if the exchange rate moves in your favour enough to more than offset the premium paid for the option.</p>

  <p class="abs price-intro">What determines the price of a Vanilla Option?<br>The cost of an option is defined by the premium that is required to be paid in order to enter into the contract. Premiums are calculated using the industry standard formulas based upon the Black Scholes model. The most important variables in the option pricing formulas include the following:</p>

  <ul class="abs factors">
    <li>•&nbsp; The current market Spot Rate.</li>
    <li>•&nbsp; Market volatility – the higher the volatility, the higher the premium.</li>
    <li>•&nbsp; The Term of the Option – a longer term typically results in a higher premium.</li>
    <li>•&nbsp; The Strike Rate – the closer to being ITM the protection rate is, the higher the premium.</li>
    <li>•&nbsp; The interest rate differential of the two currencies involved.</li>
    <li class="style">•&nbsp; Style – European or American, or whether the option can be exercised prior to expiration<br>An option can either a European (meaning that they can only be exercised on the expiry date), or American (meaning that they can be exercised at any time prior to expiration). We normally deals in European options however, we do offer American options under certain circumstances and when specific delivery terms are agreed upon between us and the customer.</li>
  </ul>
</section>

</body>
</html>
```